It must be unique & Proffessional
VORNA GROUP
# 130 Very nice, could you please use the “symbols” for Phone, cellphone and so on, instead of writing “p:” and “c:”. You did that by # 69 :-)
Thanks for all your very creative suggestions.
A general comment:
- Please correct the “projektchef” to “Direktør”
- Please add at fixed telephone number +45 62 18 37 51
- Please add “+45” in front of the cellphone number
- Please make the envelope as window envelops, and logo bottom right corner
- On the A4 paper, we need the logo in top right corner
#61,Very good design, please make the backside as you’ve done by #64
#128Please leave the bottom of the paper free of text and colors, and add only one thin line 13 mm from the page bottom.
Again very good designs, thank you very much
Logo AI file is now uploaded :-)
Now we have our Logo ready, looking forward to see your suggestions for design :-)
TK/RWF Team
Logo is currently being designed, you can participate if you would like to :-)

```html
<!DOCTYPE html>
<html lang="en">
<head>
<meta charset="utf-8">
<title>VORNA GROUP – Business Card</title>
<link rel="stylesheet" href="https://fonts.googleapis.com/css2?family=Roboto:wght@400;500;700&display=swap">
<style>
  :root {
    --bg: #ececec;
    --card: #ffffff;
    --ink: #4a4a4a;
    --ink-soft: #c9c9c9;
    --red: #c4161c;
    --red-light: #e0362c;
    --red-soft: #e9a3a3;
    --band-block: #4d4d4d;
  }
  * { margin: 0; padding: 0; box-sizing: border-box; }
  html, body { width: 1200px; height: 530px; overflow: hidden; }
  body {
    background: var(--bg);
    font-family: "Roboto", Arial, sans-serif;
    position: relative;
  }
  .card {
    position: absolute;
    top: 90px;
    width: 556px;
    height: 350px;
    background: var(--card);
    border-radius: 18px;
    overflow: hidden;
    box-shadow: 0 2px 6px rgba(0,0,0,0.12);
  }
  .card--front { left: 30px; }
  .card--back { left: 614px; }

  .brand {
    position: absolute;
    top: 88px;
    left: 0; right: 0;
    display: flex;
    justify-content: center;
    align-items: center;
    gap: 14px;
  }
  .brand__mark { width: 30px; height: 30px; background: var(--red); }
  .brand__name {
    font-size: 40px;
    font-weight: 700;
    letter-spacing: 1px;
    color: var(--ink);
  }
  .card--back .brand__mark { background: var(--red-soft); }
  .card--back .brand__name { color: var(--ink-soft); }

  .band {
    position: absolute;
    top: 200px;
    left: 0;
    width: 100%;
    height: 30px;
    display: flex;
  }
  .band__bar {
    width: 504px;
    height: 100%;
    background: linear-gradient(to right, var(--red), var(--red-light) 60%, var(--red));
    color: #fff;
    display: flex;
    align-items: center;
    justify-content: center;
    font-size: 15px;
  }
  .band__block {
    width: 30px;
    margin-left: 4px;
    height: 100%;
    background: var(--band-block);
  }
  .band__name { font-weight: 700; letter-spacing: 0.5px; }
  .band__role { font-weight: 400; margin-left: 6px; }
  .band__web { letter-spacing: 2px; font-size: 13px; }

  .contact {
    position: absolute;
    top: 250px;
    left: 0; right: 0;
    text-align: center;
    color: var(--ink);
    font-size: 13px;
    line-height: 29px;
  }
  .contact__item { margin: 0 6px; }
</style>
</head>
<body>
  <section class="card card--front">
    <div class="brand">
      <span class="brand__mark"></span>
      <span class="brand__name">VORNA GROUP</span>
    </div>
    <div class="band">
      <div class="band__bar">
        <span class="band__name">TOBIAS KROGHOLT</span>
        <span class="band__role">Direktør</span>
      </div>
      <div class="band__block"></div>
    </div>
    <div class="contact">
      <p>
        <span class="contact__item">C : +45 62 18 37 51</span>
        <span class="contact__item">E : tk@vornagroup.com</span>
        <span class="contact__item">W: www.vornagroup.com</span>
      </p>
      <p>Vestervangen 24, 7100 Vejle, Denmark</p>
    </div>
  </section>

  <section class="card card--back">
    <div class="brand">
      <span class="brand__mark"></span>
      <span class="brand__name">VORNA GROUP</span>
    </div>
    <div class="band">
      <div class="band__bar">
        <span class="band__web">www.vornagroup.com</span>
      </div>
      <div class="band__block"></div>
    </div>
  </section>
</body>
</html>
```